Bright and beautiful business card for a coach

I'm a personal and business coach based in Perth, Australia. I need a business card that whilst subtle and elegant, will stand out and appeal on a table full of cards.

My business name is Tide Mentoring and the business card must represent the warmth and brightness implied in the name, without being gimmicky. It must have a warmth and appeal and be easy to read.

I prefer clean, minimalist designs.

It must align with the feel of my website and socials: https://www.tidementoring.com.au/
https://www.instagram.com/tidementoringau/
https://www.facebook.com/tidementoringau
Updates

Hi Designers Thank you so much for taking the time to submit designs. I wonder if I could have explained myself a little better. Most of the designs that have been submitted look rather formal and many have quite corporate looking embellishments on them (to my eye). I would like softer, warmer, more organic. I’m open to people playing about and being more abstract, using softer embellishments (e.g the line drawing flowers and grasses I’ve used in my socials) incorporating other colours from my palette or like the social icons in my email signature (in PDF), perhaps playing with size/oversize, playing with the bleed. Please don’t be constrained by what I’ve already done, it merely needs to compliment. I’m sorry if I’m not using the right words or have led you astray. I’m no designer, but I’ve done my website, socials, email signature etc all myself (my logo was a design contest) and I was really hoping for my business card to be something more creative than I could have made with a template. Reminder: No black cards/sides please. Thank you 😊

Target Market(s)

Individuals, most likely but not all female. Creative thinkers. Likely professionals.

Industry/Entity Type

Business & Personal Coach

Contact Information for Business Card

(Tide Mentoring Logo) Name: Maren Delsby; Title: Business & Personal Coach; Phone number: +61 (0)438 915307; Email: maren@tidementoring.com.au; Website: https://tidementoring.com.au; Social icons for Facebook, Instagram & LinkedIn: @tidementoringAU. Optional strapline: "A thinking partner to help you cut through the noise"

Font styles to use
Sans Serif

Colors
00AB8E
00BBA5
67D7C9
C6EFE9
E9F9F6
59FF00
82FF00
B8FF75
E3FFCB
F4FFEA
FFC000
F8CF3A
FAE287
FDF2CF
FEFAEE

Requirements
Must have
• Must align with feel of my website and socials. Must have a pop of #FFC000 (possibly whole of one side, or at least a block). Bright or white background. Easy to read.
Nice to have
• Possibly incorporate the sunshine/grass picture I have used in website and socials - will upload.
Should not have
• Must not be black or dark. Not impersonal or corporate looking.

```html
<!DOCTYPE html>
<html lang="en">
<head>
<meta charset="utf-8">
<title>Tide Mentoring — Business Card</title>
<link href="https://fonts.googleapis.com/css2?family=Poppins:wght@300;400;500;600&display=swap" rel="stylesheet">
<style>
  :root {
    --backdrop: #dcdcdc;
    --card-white: #ffffff;
    --amber: #e0921c;
    --gold-band: #ffc000;
    --gold-band-edge: #e39a14;
    --ink: #2a2a2a;
    --rule: #bdbdbd;
    --grass-top: #6f8f3a;
    --grass-mid: #5f8f22;
    --grass-low: #4a7420;
  }
  * { box-sizing: border-box; margin: 0; padding: 0; }
  html, body { width: 1200px; height: 800px; overflow: hidden; }
  body {
    background: var(--backdrop);
    font-family: "Poppins", sans-serif;
    position: relative;
  }
  .card {
    position: absolute;
    top: 245px;
    width: 540px;
    height: 310px;
    border-radius: 22px;
    overflow: hidden;
    box-shadow: 0 10px 28px rgba(0,0,0,0.18);
  }
  /* Contact side */
  .card-contact { left: 45px; background: var(--card-white); }
  .brand-block {
    position: absolute;
    left: 0; top: 0;
    width: 262px; height: 310px;
    display: flex; align-items: center; justify-content: center;
  }
  .brand-name {
    font-weight: 400;
    font-size: 24px;
    letter-spacing: 0.3px;
    color: var(--amber);
    display: flex; align-items: center; gap: 9px;
    white-space: nowrap;
  }
  .brand-dot {
    width: 13px; height: 13px; border-radius: 50%;
    background: var(--amber);
    flex: none;
  }
  .divider {
    position: absolute;
    left: 262px; top: 40px;
    width: 1px; height: 230px;
    background: linear-gradient(to bottom, transparent, var(--rule) 20%, #555 50%, var(--rule) 80%, transparent);
  }
  .contact-block {
    position: absolute;
    left: 285px; top: 60px;
  }
  .person-name {
    font-size: 24px;
    font-weight: 600;
    color: var(--amber);
    line-height: 1.1;
  }
  .person-title {
    font-size: 14px;
    color: var(--ink);
    margin-bottom: 12px;
  }
  .contact-list { list-style: none; }
  .contact-list li {
    display: flex; align-items: center; gap: 9px;
    font-size: 13px;
    color: var(--ink);
    line-height: 21px;
    white-space: nowrap;
  }
  .contact-icon { width: 13px; height: 13px; flex: none; }
  .social-dot {
    width: 12px; height: 12px; border-radius: 50%;
    background: var(--amber); flex: none; margin: 0 0.5px;
  }
  /* Feature side */
  .card-feature { left: 615px; }
  .feature-photo {
    position: absolute; inset: 0;
    background: linear-gradient(to bottom, var(--grass-top) 0%, var(--grass-mid) 55%, var(--grass-low) 100%);
  }
  .feature-brand {
    position: absolute;
    left: 0; right: 0; top: 110px;
    display: flex; justify-content: center;
  }
  .feature-brand .brand-name { color: #ffffff; font-size: 30px; }
  .feature-brand .brand-dot { background: #ffffff; }
  .strap-band {
    position: absolute;
    left: 0; right: 0; top: 232px;
    height: 32px;
    background: linear-gradient(to right, var(--gold-band-edge), var(--gold-band) 50%, var(--gold-band-edge));
    display: flex; align-items: center; justify-content: center;
  }
  .strapline {
    font-size: 14.5px;
    font-weight: 500;
    color: var(--ink);
    white-space: nowrap;
  }
</style>
</head>
<body>

<section class="card card-contact">
  <div class="brand-block">
    <div class="brand-name"><span class="brand-dot"></span>Tide Mentoring</div>
  </div>
  <div class="divider"></div>
  <div class="contact-block">
    <h1 class="person-name">Maren Delsby</h1>
    <p class="person-title">Business &amp; Personal Coach</p>
    <ul class="contact-list">
      <li>
        <svg class="contact-icon" viewBox="0 0 24 24"><path fill="var(--amber)" d="M6.6 10.8a15 15 0 0 0 6.6 6.6l2.2-2.2c.3-.3.7-.4 1-.2 1.1.4 2.3.6 3.6.6.6 0 1 .4 1 1V20c0 .6-.4 1-1 1A17 17 0 0 1 3 4c0-.6.4-1 1-1h3.5c.6 0 1 .4 1 1 0 1.3.2 2.5.6 3.6.1.3 0 .7-.2 1z"/></svg>
        +61 (0)438 915307
      </li>
      <li>
        <svg class="contact-icon" viewBox="0 0 24 24"><rect x="2" y="5" width="20" height="14" rx="2" fill="var(--amber)"/><path d="M3 6l9 7 9-7" stroke="#fff" stroke-width="1.8" fill="none"/></svg>
        maren@tidementoring.com.au
      </li>
      <li>
        <svg class="contact-icon" viewBox="0 0 24 24"><circle cx="12" cy="12" r="10" fill="var(--amber)"/><path d="M2.5 12h19M12 2.5c3 3 3 16 0 19M12 2.5c-3 3-3 16 0 19" stroke="#fff" stroke-width="1.4" fill="none"/></svg>
        www.tidementoring.com.au
      </li>
      <li><span class="social-dot"></span>/tidementoringAU</li>
      <li><span class="social-dot"></span>@tidementoringAU</li>
      <li><span class="social-dot"></span>/tidementoringAU</li>
    </ul>
  </div>
</section>

<section class="card card-feature">
  <div class="feature-photo" role="img" aria-label="Photograph of sunlit green grass with sunshine through trees"></div>
  <div class="feature-brand">
    <div class="brand-name"><span class="brand-dot"></span>Tide Mentoring</div>
  </div>
  <div class="strap-band">
    <p class="strapline">A thinking partner to help you cut through the noise</p>
  </div>
</section>

</body>
</html>
```